business card design and letterhead for a building inspection company. We have a pre-purchase building and pest inspection ( i inspect house before people purchase it)
Updates

Tilda has been so so responsive and good, i highly recommend her

Industry/Entity Type

Building

Contact Information for Business Card

audience, solicitor, real estate agent, mortgage brokerthe rest of the info will be in the attachement business card

```html
<!DOCTYPE html>
<html lang="en">
<head>
<meta charset="utf-8">
<title>Clearview Property Inspections – Business Card</title>
<link rel="stylesheet" href="https://fonts.googleapis.com/css2?family=Exo+2:wght@700&family=Share+Tech+Mono&display=swap">
<style>
  :root {
    --brand-blue: #1b6fc4;
    --card-white: #ffffff;
    --ink-dark: #2a2f36;
    --backdrop: #eceef0;
    --icon-tint: #a9cdf0;
  }
  html, body {
    margin: 0;
    width: 1200px;
    height: 873px;
    overflow: hidden;
    background: var(--backdrop);
  }
  .sheet {
    position: relative;
    width: 1200px;
    height: 873px;
  }
  .card {
    position: absolute;
    left: 320px;
    width: 560px;
    height: 320px;
    background: var(--card-white);
    overflow: hidden;
    box-shadow: 0 2px 10px rgba(0,0,0,0.12);
  }
  .card--front { top: 86px; }
  .card--back  { top: 466px; }

  .band {
    position: absolute;
    left: 0; right: 0; bottom: 22px;
    height: 34px;
    background: var(--brand-blue);
    color: var(--card-white);
    font-family: "Share Tech Mono", monospace;
    font-size: 16px;
    letter-spacing: 3px;
    display: flex;
    align-items: center;
    padding-left: 24px;
  }
  .ring {
    position: absolute;
    border: 22px solid var(--brand-blue);
    border-radius: 50%;
    box-sizing: border-box;
    display: flex;
    flex-direction: column;
    align-items: center;
    justify-content: center;
    text-align: center;
    background: var(--card-white);
  }
  .card--front .ring { left: 150px; top: 14px; width: 240px; height: 240px; }
  .card--back .ring  { left: 290px; top: 26px; width: 230px; height: 230px; }

  .brand-name {
    font-family: "Exo 2", sans-serif;
    font-weight: 700;
    color: var(--brand-blue);
    letter-spacing: 1px;
    line-height: 1;
  }
  .brand-name--large { font-size: 30px; }
  .brand-sub {
    font-family: "Share Tech Mono", monospace;
    color: var(--ink-dark);
    font-size: 12px;
    letter-spacing: 1px;
    margin-top: 3px;
  }
  .brand-tagline {
    font-family: "Share Tech Mono", monospace;
    color: var(--brand-blue);
    font-size: 10px;
    margin-top: 2px;
  }
  .brand-web {
    font-family: "Share Tech Mono", monospace;
    color: var(--ink-dark);
    font-size: 9px;
    margin-top: 4px;
  }

  .back-logo {
    position: absolute;
    left: 24px; top: 24px;
    display: flex;
    align-items: center;
    gap: 10px;
  }
  .back-logo .marker {
    width: 18px; height: 18px;
    background: var(--brand-blue);
  }
  .back-logo .brand-name { font-size: 24px; }
  .back-logo .brand-sub { font-size: 10px; }

  .house-icons {
    position: absolute;
    left: 40px; top: 150px;
    width: 120px; height: 70px;
    background: var(--icon-tint);
  }
  .divider {
    position: absolute;
    left: 0; top: 0;
  }
  .person-name {
    font-family: "Exo 2", sans-serif;
    font-weight: 700;
    color: var(--brand-blue);
    font-size: 22px;
    letter-spacing: 1px;
  }
  .contact-line {
    font-family: "Share Tech Mono", monospace;
    color: var(--ink-dark);
    font-size: 11px;
    margin-top: 4px;
  }
</style>
</head>
<body>
<main class="sheet">

  <section class="card card--front">
    <div class="ring">
      <div class="brand-name brand-name--large">CLEARVIEW</div>
      <div class="brand-sub">PROPERTY INSPECTIONS</div>
      <div class="brand-tagline">building and pest experts</div>
      <div class="brand-web">WWW.CLEARVIEWINSPECT.COM.AU</div>
    </div>
    <div class="band">PROPERTY INSPECTION | PROPERTY MANAGEMENT</div>
  </section>

  <section class="card card--back">
    <svg class="divider" width="560" height="320" viewBox="0 0 560 320" aria-hidden="true">
      <line x1="20" y1="78" x2="560" y2="150" stroke="var(--brand-blue)" stroke-width="3"/>
    </svg>
    <div class="back-logo">
      <span class="marker"></span>
      <div>
        <div class="brand-name">CLEARVIEW</div>
        <div class="brand-sub">PROPERTY INSPECTIONS</div>
      </div>
    </div>
    <div class="house-icons" role="img" aria-label="Row of house roof outlines with check marks"></div>
    <div class="ring">
      <div class="person-name">SARAH TILDA</div>
      <div class="contact-line">INFO@CLEARVIEWINSPECT.COM.AU</div>
      <div class="contact-line">(02) 5550 1840</div>
      <div class="contact-line">0400 555 019</div>
    </div>
    <div class="band">WWW.CLEARVIEWINSPECT.COM.AU</div>
  </section>

</main>
</body>
</html>
```